New business card design to go with our new logo

just want an eye-catching business card to go with our new logo. We are open to double sided or single sided. Just want it to have the following info on it. Whatever layout you think looks best.

First and Last Name
Title
Phone 801-555-0187
Address 312 W. Larkmoor Avenue Orem UT 84057
Email thecrew@meadowstailandkennel.example

Industry/Entity Type

Business

```html
<!DOCTYPE html>
<html lang="en">
<head>
<meta charset="utf-8">
<title>Meadows Tail &amp; Kennel — Business Card</title>
<link href="https://fonts.googleapis.com/css2?family=Marcellus+SC&family=Lato:wght@400;700&display=swap" rel="stylesheet">
<style>
  :root {
    --stage: #555555;
    --card-white: #ffffff;
    --brand-blue: #2ea6d9;
    --brand-orange: #f0874a;
    --ink: #3f3f3f;
    --rule: #bdbdbd;
  }
  * { margin: 0; padding: 0; box-sizing: border-box; }
  html, body { width: 1200px; height: 900px; overflow: hidden; }
  body { background: var(--stage); position: relative; font-family: "Lato", sans-serif; }

  .card { position: absolute; top: 170px; width: 347px; height: 561px; }
  .card-front { left: 259px; background: var(--card-white); }
  .card-back { left: 631px; background: var(--brand-blue); }

  .brand-name {
    position: absolute; left: 0; width: 100%; text-align: center;
    font-family: "Marcellus SC", serif; font-weight: 400; line-height: 1.1;
  }
  .card-front .brand-name { top: 222px; font-size: 30px; color: var(--brand-orange); }
  .card-back .brand-name { top: 428px; font-size: 36px; color: var(--card-white); }

  .brand-mark {
    position: absolute; left: 134px; top: 115px; width: 80px; height: 80px;
    border-radius: 50%; background: var(--brand-orange);
  }

  .contact {
    position: absolute; left: 0; top: 368px; width: 100%; text-align: center; color: var(--ink);
  }
  .person-name {
    font-family: "Marcellus SC", serif; font-size: 20px; line-height: 24px; letter-spacing: 0.5px;
  }
  .person-name .first { color: var(--brand-orange); }
  .person-name .last { color: var(--brand-blue); }
  .person-title { font-size: 15px; line-height: 18px; }
  .divider { width: 137px; height: 1px; background: var(--rule); margin: 10px auto 12px; }
  .address, .lines { font-size: 15px; line-height: 20px; }
  .lines { margin-top: 10px; }
</style>
</head>
<body>
  <section class="card card-front">
    <div class="brand-mark"></div>
    <div class="brand-name">Meadows Tail<br>&amp; Kennel</div>
    <div class="contact">
      <p class="person-name"><span class="first">Daniel</span> <span class="last">Harlow</span></p>
      <p class="person-title">Managing Director</p>
      <div class="divider"></div>
      <p class="address">312 W. Larkmoor Avenue<br>Orem UT 84057</p>
      <p class="lines">801-555-0187<br>thecrew@meadowstailandkennel.example</p>
    </div>
  </section>

  <section class="card card-back">
    <div class="brand-name">Meadows Tail<br>&amp; Kennel</div>
  </section>
</body>
</html>
```